RW dental business card. A family dental practice.

Logo plus the following details.

RW Dental
Dr. Marcus Ellory D.D.S
Family. Implant.Cosmetic

48 Fernbrook Lane, Unit 12-13
Markham, ON K2P7R4

Tel: 905-318-2670
Fx:905-318-9025
rwdental-sample.ca

On the double side:

Next app: ______________________

Please notify us at least 48hours in advance to avoid cancellation fees.

Target Market(s)

Family Dental Services

Industry/Entity Type

Dental

Contact Information for Business Card

Put logo prominently and all the info along with it.

Font styles to use
Other font styles liked:
• See Logo Font

Colors
0255a3
3277b5
85acd3
00a990
33b8a4

Requirements
Must have
• Logo and the info stated above.
• See the logo color scheme.
• Or a grayscale (Black, white gray) combination
Nice to have
• A modern unique layout
Should not have
• too simple a design

```html
<!DOCTYPE html>
<html lang="en">
<head>
<meta charset="utf-8">
<title>RW Dental – Business Card</title>
<link rel="stylesheet" href="https://fonts.googleapis.com/css2?family=Source+Sans+3:ital,wght@0,400;0,600;0,700;1,400&display=swap">
<style>
  :root {
    --navy: #04467f;
    --navy-text: #0d4a86;
    --white: #ffffff;
    --mint: #b3e6e6;
    --backdrop: #ecebe7;
    --shadow: rgba(40, 30, 20, 0.28);
  }
  * { box-sizing: border-box; margin: 0; padding: 0; }
  html, body {
    width: 1008px; height: 1200px; overflow: hidden;
    background: var(--backdrop);
    font-family: "Source Sans 3", "Myriad Pro", sans-serif;
  }
  .card {
    position: absolute; width: 794px; height: 464px;
    border-radius: 40px; overflow: hidden;
    box-shadow: 0 6px 18px var(--shadow);
  }
  .card--front { left: 107px; top: 93px; background: var(--navy); color: var(--white); }
  .card--back { left: 115px; top: 628px; background: var(--white); color: var(--navy-text); }

  /* Front */
  .brand { position: absolute; left: 100px; top: 36px; width: 270px; text-align: center; }
  .brand__mark {
    display: block; margin: 0 auto 12px; width: 54px; height: 54px;
    border: 4px solid var(--white); border-radius: 50%;
  }
  .brand__name { font-size: 34px; font-weight: 600; line-height: 1; }
  .brand__tagline { font-size: 18px; margin-top: 9px; }

  .doctor { position: absolute; right: 417px; top: 255px; text-align: right; }
  .doctor__name { font-size: 22px; font-weight: 700; }
  .doctor__focus { font-size: 20px; margin-top: 9px; }

  .divider { position: absolute; left: 394px; top: 238px; width: 2px; height: 164px; background: var(--white); }

  .contact { position: absolute; left: 418px; top: 238px; list-style: none; font-size: 21px; line-height: 1.3; }
  .contact li { display: flex; align-items: flex-start; margin-bottom: 5px; }
  .contact__icon { width: 22px; height: 22px; margin: 2px 6px 0 0; flex: none; fill: var(--white); }
  .contact__address { margin-bottom: 8px !important; }

  /* Back */
  .appointment__title {
    position: absolute; left: 0; width: 754px; top: 64px; text-align: center;
    font-size: 23px; font-weight: 700; letter-spacing: 2px;
  }
  .appointment__fields { position: absolute; left: 94px; top: 118px; list-style: none; font-size: 18px; }
  .appointment__fields li { display: flex; align-items: flex-end; height: 53px; }
  .appointment__line { display: inline-block; width: 480px; border-bottom: 1.5px solid var(--navy-text); margin-left: 6px; height: 16px; }
  .appointment__notice {
    position: absolute; left: 0; width: 794px; top: 394px; text-align: center;
    font-size: 22px; font-style: italic;
  }
  .watermark-circle {
    position: absolute; left: 636px; top: 20px; width: 290px; height: 290px;
    border-radius: 50%; border: 16px solid var(--mint);
  }
  .watermark-name {
    position: absolute; left: 662px; top: 150px;
    font-size: 24px; font-weight: 600; color: var(--mint);
    white-space: nowrap;
  }
</style>
</head>
<body>

<section class="card card--front">
  <div class="brand">
    <span class="brand__mark"></span>
    <div class="brand__name">RW Dental</div>
    <div class="brand__tagline">Your dental health support Team</div>
  </div>

  <div class="doctor">
    <div class="doctor__name">DR. Marcus Ellory D.D.S.</div>
    <div class="doctor__focus">Family. Implant. Cosmetic</div>
  </div>

  <div class="divider"></div>

  <ul class="contact">
    <li class="contact__address">
      <svg class="contact__icon" viewBox="0 0 24 24"><path d="M12 2 1 10h3v11h16V10h3L12 2zm-5 10h10v7H7v-7zm2 2v3h6v-3H9z"/></svg>
      <span>48 Fernbrook Lane, Unit 12-13<br>Markham, ON K2P7R4</span>
    </li>
    <li>
      <svg class="contact__icon" viewBox="0 0 24 24"><path d="M6.6 10.8a15.1 15.1 0 0 0 6.6 6.6l2.2-2.2c.3-.3.7-.4 1-.2 1.1.4 2.3.6 3.6.6.6 0 1 .4 1 1V20c0 .6-.4 1-1 1A17 17 0 0 1 3 4c0-.6.4-1 1-1h3.5c.6 0 1 .4 1 1 0 1.3.2 2.5.6 3.6.1.3 0 .7-.2 1l-2.3 2.2z"/></svg>
      <span>905-318-2670</span>
    </li>
    <li>
      <svg class="contact__icon" viewBox="0 0 24 24"><path d="M6 2h10v6H6V2zm2 2v2h6V4H8zM3 9h18v9H3V9zm3 2v2h2v-2H6zm4 0v2h2v-2h-2zm4 0v2h4v-2h-4zM2 19h20v3H2v-3z"/></svg>
      <span>905-318-9025</span>
    </li>
    <li>
      <svg class="contact__icon" viewBox="0 0 24 24"><path d="M12 2a10 10 0 1 0 0 20 10 10 0 0 0 0-20zm0 2c.9 0 2.2 1.9 2.7 5H9.3C9.8 5.9 11.1 4 12 4zM9.6 4.5C8.8 5.7 8.3 7.3 8 9H4.8a8 8 0 0 1 4.8-4.5zm4.8 0A8 8 0 0 1 19.2 9H16c-.3-1.7-.8-3.3-1.6-4.5zM4.2 11h3.6a18 18 0 0 0 0 2H4.2a8 8 0 0 1 0-2zm5.6 0h4.4a16 16 0 0 1 0 2H9.8a16 16 0 0 1 0-2zm6.4 0h3.6a8 8 0 0 1 0 2h-3.6a18 18 0 0 0 0-2zM4.8 15H8c.3 1.7.8 3.300 1.6 4.5A8 8 0 0 1 4.8 15zm4.5 0h5.4c-.5 3.1-1.8 5-2.7 5s-2.2-1.9-2.7-5zm6.7 0h3.2a8 8 0 0 1-4.8 4.5c.8-1.2 1.3-2.8 1.6-4.5z"/></svg>
      <span>www.rwdental-sample.ca</span>
    </li>
  </ul>
</section>

<section class="card card--back">
  <span class="watermark-circle"></span>
  <span class="watermark-name">RW Dental</span>

  <h2 class="appointment__title">NEXT APPOINTMENT:</h2>
  <ul class="appointment__fields">
    <li>Date <span class="appointment__line"></span></li>
    <li>Time <span class="appointment__line"></span></li>
    <li>Date <span class="appointment__line"></span></li>
    <li>Time <span class="appointment__line"></span></li>
  </ul>
  <p class="appointment__notice">Please notify us at least 48hours in advance to avoid cancellation fees.</p>
</section>

</body>
</html>
```